Business Card for Lorena Whitfield

Name: Lorena Whitfield
Title: Realtor
Email: Lorena@LorenaWhitfieldRE.com
Phone: 480-555-0137

On the front of the business card, I would like the photo, the contact information and the Lorena Whitfield Logo. The backside is required to have the Broker logo and the required logos. Please use the colors from the logo design. Our company has a classy, professional look.

```html
<!DOCTYPE html>
<html lang="en">
<head>
<meta charset="utf-8">
<title>Lorena Whitfield Real Estate – Business Card</title>
<link rel="stylesheet" href="https://fonts.googleapis.com/css2?family=Cinzel:wght@500;600&family=Tinos:wght@400&display=swap">
<style>
  :root{
    --backdrop:#6a6767;
    --card:#fbfbfb;
    --ink:#3b3b3d;
    --ink-soft:#5a5a5c;
    --crimson:#a3162c;
    --photo-light:#d9d9d9;
    --photo-dark:#4a4a4a;
    --badge:#6d6d6f;
  }
  *{box-sizing:border-box;margin:0;padding:0}
  html,body{width:1200px;height:1200px;overflow:hidden}
  body{background:var(--backdrop);position:relative;font-family:"Tinos",serif;color:var(--ink)}

  .card{position:absolute;width:594px;height:344px;background:var(--card);border-radius:18px;overflow:hidden}

  /* Back side */
  .card--back{left:298px;top:200px;border-bottom:6px solid var(--crimson)}
  .broker-mark{position:absolute;left:0;right:0;top:52px;display:flex;flex-direction:column;align-items:center}
  .broker-mark__circle{width:112px;height:112px;border-radius:50%;border:3px solid var(--ink-soft)}
  .broker-mark__name{margin-top:26px;font-family:"Cinzel",serif;font-weight:600;font-size:19px;letter-spacing:2.5px;color:var(--ink)}
  .broker-mark__sub{font-family:"Cinzel",serif;font-weight:600;font-size:10px;letter-spacing:1.5px;color:var(--ink)}
  .compliance{position:absolute;left:128px;top:254px;display:flex;gap:6px}
  .compliance__badge{width:44px;height:40px;border:2px solid var(--badge);border-radius:2px}
  .compliance__badge--wide{width:76px}
  .back-web{position:absolute;left:277px;top:268px;font-size:16px;color:var(--ink)}
  .back-web span{color:var(--crimson)}

  /* Front side */
  .card--front{left:292px;top:637px;height:348px}
  .agent-mark{position:absolute;left:30px;top:38px;display:flex;align-items:center;gap:12px;color:var(--crimson)}
  .agent-mark__square{width:64px;height:64px;border:3px solid var(--crimson)}
  .agent-mark__text{font-family:"Cinzel",serif;font-weight:500;line-height:1}
  .agent-mark__name{font-size:26px;letter-spacing:.5px}
  .agent-mark__sub{font-size:12px;letter-spacing:1.5px;margin-top:6px;text-align:right}

  .portrait{position:absolute;right:0;top:0;width:210px;height:234px;background:linear-gradient(180deg,var(--photo-light) 0%,#a9a9a9 55%,var(--photo-dark) 100%)}

  .agent-name{position:absolute;left:29px;top:178px;font-family:"Cinzel",serif;font-weight:500;font-size:22px;letter-spacing:1px;color:var(--ink)}
  .agent-title{position:absolute;left:29px;top:216px;font-size:15px;color:var(--crimson)}
  .divider{position:absolute;left:0;top:0}

  .contacts{position:absolute;left:30px;top:256px;list-style:none}
  .contacts li{display:flex;align-items:center;gap:14px;height:23px;font-size:15.5px;color:var(--ink)}
  .contacts svg{width:12px;height:12px;fill:var(--crimson)}

  .broker-mini{position:absolute;left:488px;top:250px;width:92px;display:flex;flex-direction:column;align-items:center}
  .broker-mini__circle{width:40px;height:40px;border-radius:50%;border:2px solid var(--ink-soft)}
  .broker-mini__name{margin-top:8px;font-family:"Cinzel",serif;font-weight:600;font-size:7.5px;letter-spacing:.8px;color:var(--ink);text-align:center;line-height:1.2}
</style>
</head>
<body>

<section class="card card--back" aria-label="Business card back">
  <div class="broker-mark">
    <div class="broker-mark__circle"></div>
    <div class="broker-mark__name">HARRINGTON REED</div>
    <div class="broker-mark__sub">REAL ESTATE</div>
  </div>
  <div class="compliance">
    <div class="compliance__badge" aria-label="Housing badge"></div>
    <div class="compliance__badge compliance__badge--wide" aria-label="Listing service badge"></div>
  </div>
  <p class="back-web">www.<span>LorenaWhitfieldRE.com</span></p>
</section>

<section class="card card--front" aria-label="Business card front">
  <div class="agent-mark">
    <div class="agent-mark__square"></div>
    <div class="agent-mark__text">
      <div class="agent-mark__name">LORENA WHITFIELD</div>
      <div class="agent-mark__sub">REAL ESTATE</div>
    </div>
  </div>

  <div class="portrait" role="img" aria-label="Portrait photo of Lorena Whitfield"></div>

  <svg class="divider" width="594" height="348" viewBox="0 0 594 348" aria-hidden="true">
    <path d="M0 211 H290 C318 211 330 234 360 234 H384" fill="none" stroke="var(--crimson)" stroke-width="1.5"/>
  </svg>

  <h1 class="agent-name">LORENA WHITFIELD</h1>
  <p class="agent-title">Realtor/Broker</p>

  <ul class="contacts">
    <li><svg viewBox="0 0 12 12"><path d="M1 4c0-2 2-3 5-3s5 1 5 3v1H8V3.8H4V5H1z M2.5 6h7l1 5h-9z"/></svg>480-555-0137</li>
    <li><svg viewBox="0 0 12 12"><path d="M0 2h12v8H0z M1 3l5 3.5L11 3v-.2H1z" fill-rule="evenodd"/></svg>Lorena@LorenaWhitfieldRE.com</li>
    <li><svg viewBox="0 0 12 12"><path d="M6 0a6 6 0 1 0 0 12A6 6 0 0 0 6 0zm0 1.3c.9 0 1.8 2 1.9 4H4.1c.1-2 1-4 1.9-4zM1.3 5.3a4.8 4.8 0 0 1 2.1-3.4c-.4 1-.6 2.2-.7 3.4zm0 1.4h1.4c.1 1.2.3 2.4.7 3.4a4.8 4.8 0 0 1-2.1-3.4zm4.7 4c-.9 0-1.8-2-1.9-4h3.8c-.1 2-1 4-1.9 4zm2.6-.6c.4-1 .6-2.2.7-3.4h1.4a4.8 4.8 0 0 1-2.1 3.4zm.7-4.8c-.1-1.2-.3-2.4-.7-3.4a4.8 4.8 0 0 1 2.1 3.4z"/></svg>www.LorenaWhitfieldRE.com</li>
  </ul>

  <div class="broker-mini">
    <div class="broker-mini__circle"></div>
    <div class="broker-mini__name">HARRINGTON REED<br>REAL ESTATE</div>
  </div>
</section>

</body>
</html>
```